Ridgeline Talent Associates Business Card Design

We need a business card design for our new company - Ridgeline Talent Associates. RLTA is a recruitment firm that focuses on recruiting engineers and geologist for mid-size oil and gas companies. We would like our logo on the business card, which is attached, and we would like the color scheme on business cards to coordinate with our logo.

Industry/Entity Type

Oil And Gas

Contact Information for Business Card

Dana Whitlow, Founder and Managing Partner, dmw@ridgelinetalentco.org, 888.507.3942 (work), 5730915.0600 (cell), 573.642.1907 (fax), www.ridgelinetalentco.org

```html
<!DOCTYPE html>
<html lang="en">
<head>
<meta charset="utf-8">
<title>Ridgeline Talent Associates – Business Card</title>
<link href="https://fonts.googleapis.com/css2?family=Arimo:wght@400;700&display=swap" rel="stylesheet">
<style>
  :root {
    --backdrop: #e9e6e2;
    --card: #ffffff;
    --band-soft: #f1f2f4;
    --navy: #33407d;
    --navy-deep: #2a3670;
    --navy-light: #44528c;
    --rule: #2b2b2f;
    --ink-muted: #4a4a55;
    --white: #ffffff;
  }
  * { box-sizing: border-box; margin: 0; padding: 0; }
  html, body { width: 1200px; height: 914px; overflow: hidden; }
  body {
    background: var(--backdrop);
    font-family: "Arimo", Arial, sans-serif;
    position: relative;
  }
  .card {
    position: absolute;
    width: 620px;
    height: 354px;
    background: var(--card);
    box-shadow: 0 6px 18px rgba(0,0,0,.18);
    overflow: hidden;
  }
  .card--back { left: 520px; top: 70px; }
  .card--front { left: 60px; top: 470px; }

  /* back */
  .back-band {
    position: absolute; left: 0; right: 0; top: 92px; height: 170px;
    background: var(--band-soft);
  }
  .brand {
    position: absolute;
    display: flex; align-items: center; gap: 10px;
    color: var(--navy);
    font-weight: 700;
    letter-spacing: .02em;
  }
  .brand__dot {
    width: 22px; height: 22px; border-radius: 50%;
    background: var(--navy); flex: none;
  }
  .card--back .brand { left: 50%; top: 50%; transform: translate(-50%, -50%); font-size: 24px; }
  .card--front .brand { left: 38px; top: 62px; font-size: 20px; }

  /* front */
  .holder { position: absolute; left: 388px; top: 88px; color: var(--navy); }
  .holder__name { font-size: 24px; font-weight: 400; }
  .holder__role { font-size: 14px; color: var(--ink-muted); margin-top: 4px; }

  .band {
    position: absolute; left: 0; right: 0; top: 142px; height: 146px;
    background: linear-gradient(100deg, var(--navy-deep), var(--navy-light) 55%, var(--navy));
    border-top: 3px solid var(--white);
    border-bottom: 3px solid var(--white);
    outline: 2px solid var(--rule);
  }
  .contacts {
    position: absolute; list-style: none;
    color: var(--white); font-size: 15px;
  }
  .contacts li { display: flex; align-items: center; gap: 10px; height: 25px; }
  .contacts svg { width: 14px; height: 14px; flex: none; }
  .contacts--office { left: 40px; top: 16px; }
  .contacts--direct { left: 362px; top: 62px; }
</style>
</head>
<body>

<section class="card card--back" aria-label="Card back">
  <div class="back-band"></div>
  <div class="brand"><span class="brand__dot"></span>Ridgeline Talent Associates</div>
</section>

<section class="card card--front" aria-label="Card front">
  <div class="brand"><span class="brand__dot"></span>Ridgeline Talent Associates</div>

  <div class="holder">
    <p class="holder__name">Dana Whitlow</p>
    <p class="holder__role">Founder and Managing Partner</p>
  </div>

  <div class="band">
    <ul class="contacts contacts--office">
      <li>
        <svg viewBox="0 0 14 14" aria-hidden="true"><rect x="2" y="1" width="10" height="12" fill="none" stroke="#fff" stroke-width="1.4"/><path d="M5 4h1M8 4h1M5 7h1M8 7h1M5 10h1M8 10h1" stroke="#fff" stroke-width="1.4"/></svg>
        888.507.3942
      </li>
      <li>
        <svg viewBox="0 0 14 14" aria-hidden="true"><rect x="1" y="5" width="12" height="6" rx="1" fill="#fff"/><rect x="3.5" y="2" width="7" height="3" fill="#fff"/><rect x="3.5" y="10" width="7" height="3" fill="none" stroke="#fff"/></svg>
        5730915.0600
      </li>
    </ul>

    <ul class="contacts contacts--direct">
      <li>
        <svg viewBox="0 0 14 14" aria-hidden="true"><rect x="2.5" y="1" width="9" height="12" rx="2" fill="none" stroke="#fff" stroke-width="1.4"/></svg>
        5730915.0600
      </li>
      <li>
        <svg viewBox="0 0 14 14" aria-hidden="true"><rect x="1" y="3" width="12" height="8" fill="none" stroke="#fff" stroke-width="1.3"/><path d="M1 3l6 5 6-5" fill="none" stroke="#fff" stroke-width="1.3"/></svg>
        dmw@ridgelinetalentco.org
      </li>
      <li>
        <svg viewBox="0 0 14 14" aria-hidden="true"><circle cx="7" cy="7" r="5.8" fill="none" stroke="#fff" stroke-width="1.3"/><ellipse cx="7" cy="7" rx="2.4" ry="5.8" fill="none" stroke="#fff"/><path d="M1.2 7h11.6" stroke="#fff"/></svg>
        www.ridgelinetalentco.org
      </li>
    </ul>
  </div>
</section>

</body>
</html>
```